Zielgruppe
Wir sind ein Fachpflegedienst für außerklinische Intensivpflege. Unsere Zielgruppe sind Patienten, Angehörige, Krankenkassen und Kliniken
Aufgabenstellung
Wir benötigen ein ansprechendes Briefpapier. Das Design soll zu unserer Webseite und unserer Broschüre passen. Die Webseite ist www.korvalin37.de und die Broschüre ist im Anhang. Wichtig ist, dass die Badges auf dem Briefpapier zu sehen sind.

```html
<!DOCTYPE html>
<html lang="de">
<head>
<meta charset="utf-8">
<title>Korvalin Pflegedienst – Briefpapier</title>
<link href="https://fonts.googleapis.com/css2?family=Roboto:wght@400;700&display=swap" rel="stylesheet">
<style>
  :root {
    --bg: #e4e4e4;
    --paper: #d8dde5;
    --brand-red: #d0323a;
    --rule: #e9b7b9;
    --ink: #3a3d44;
    --badge-dark: #3d3f46;
    --badge-navy: #3b4a8a;
    --badge-light: #9fb6de;
    --badge-gold: #e5b43a;
    --sign: #b9bec8;
  }
  * { box-sizing: border-box; margin: 0; padding: 0; }
  html, body {
    width: 1200px; height: 1200px; overflow: hidden;
    background: var(--bg);
    font-family: "Roboto", Arial, sans-serif;
  }
  .letterhead {
    position: absolute; left: 204px; top: 40px;
    width: 792px; height: 1120px;
    background: var(--paper);
    box-shadow: 0 6px 24px rgba(0,0,0,.12);
  }
  .brand {
    position: absolute; left: 78px; top: 160px;
    display: flex; align-items: center; gap: 10px;
  }
  .brand-dot { width: 14px; height: 14px; border-radius: 50%; background: var(--brand-red); }
  .brand-name { font-weight: 400; font-size: 22px; color: var(--ink); }
  .badges {
    position: absolute; right: 70px; top: 80px;
    display: flex; gap: 30px; align-items: center;
  }
  .badge { width: 46px; height: 46px; }
  .badge-round { border-radius: 50%; background: var(--badge-dark); }
  .badge-square { background: var(--badge-navy); }
  .badge-seal { border-radius: 50%; border: 3px solid var(--badge-light); background: #eef2f8; }
  .badge-rating { height: 26px; width: 58px; border-radius: 4px; background: var(--badge-gold); opacity: .8; }
  .writing-lines { position: absolute; left: 160px; top: 330px; width: 560px; }
  .writing-lines span {
    display: block; height: 1px; background: var(--rule); margin-bottom: 44px;
  }
  .writing-lines span.short { width: 68%; }
  .contact {
    position: absolute; right: 70px; top: 905px;
    list-style: none; font-size: 13px; color: var(--ink);
  }
  .contact li { display: flex; align-items: center; gap: 12px; margin-bottom: 9px; }
  .contact svg { width: 18px; height: 18px; }
  .signatory { position: absolute; left: 78px; top: 975px; }
  .signatory-name { font-weight: 700; font-size: 19px; color: var(--brand-red); }
  .signatory-role { font-size: 15px; color: var(--brand-red); margin-top: 3px; }
  .signature { width: 110px; height: 40px; margin-top: 16px; background: var(--sign); border-radius: 20px; opacity: .55; }
</style>
</head>
<body>
  <main class="letterhead">
    <div class="brand">
      <span class="brand-dot"></span>
      <span class="brand-name">Korvalin Pflegedienst</span>
    </div>

    <div class="badges" aria-label="Auszeichnungen">
      <div class="badge badge-round" role="img" aria-label="Empfehlungssiegel"></div>
      <div class="badge badge-square" role="img" aria-label="Arbeitgeber-Auszeichnung"></div>
      <div class="badge badge-seal" role="img" aria-label="Zertifikatssiegel"></div>
      <div class="badge badge-rating" role="img" aria-label="Bewertungsplakette"></div>
    </div>

    <div class="writing-lines" aria-hidden="true">
      <span></span><span></span><span></span><span></span><span></span><span></span>
      <span></span><span></span><span></span><span></span><span class="short"></span>
    </div>

    <ul class="contact">
      <li>
        <svg viewBox="0 0 18 18"><circle cx="9" cy="9" r="8" fill="none" stroke="var(--brand-red)" stroke-width="1.3"/><path d="M6.5 5.5l1.3-.3 1 2-.8.8a5 5 0 0 0 2 2l.8-.8 2 1-.3 1.3c-3 .4-6.4-3-6-6z" fill="var(--brand-red)"/></svg>
        (04127) - 482 93 10
      </li>
      <li>
        <svg viewBox="0 0 18 18"><circle cx="9" cy="9" r="8" fill="none" stroke="var(--brand-red)" stroke-width="1.3"/><rect x="5" y="6.2" width="8" height="5.6" fill="var(--brand-red)"/><path d="M5 6.4l4 3 4-3" fill="none" stroke="var(--paper)" stroke-width=".9"/></svg>
        info@korvalin37.de
      </li>
      <li>
        <svg viewBox="0 0 18 18"><circle cx="9" cy="9" r="8" fill="none" stroke="var(--brand-red)" stroke-width="1.3"/><rect x="5.5" y="7" width="7" height="5" fill="var(--brand-red)"/><rect x="7" y="5" width="4" height="2" fill="var(--brand-red)"/></svg>
        (04127) - 482 93 12
      </li>
    </ul>

    <div class="signatory">
      <p class="signatory-name">Marten Olvesko LL.M.</p>
      <p class="signatory-role">Geschäftsführer</p>
      <div class="signature" role="img" aria-label="Handschriftliche Unterschrift"></div>
    </div>
  </main>
</body>
</html>
```